BrXpertz Business Cards for SME Experts

We need a business card for a new company based in Clearwater FL called Kestrel of Merit. KoM is your access to on-demand subject matter experts. The final design should be very clean communicating innovation and expertise. Our logo design is attached.

The Information Age has affected the workforce in that automation and computerization have resulted in higher productivity coupled with net job loss of many knowledgeable employees. Combined with the creation of the internet and search capabilities, the disintermediation of the value chain of Subject Matter Experts (SME) has happened. We no longer need to work through traditional consulting firms for all consulting needs, instead the direct access to the SME, through a leaner and lower cost model is what the market is demanding.
BrXpertz is a new marketplace to buy consulting services. The business model is that all consultants (subject matter experts) can become a consulting resource in the marketplace following our guidelines. The consumer can now easily access consultants that they could not find easily before.
In much the way an Zyla car can be identified and requested, so can a BrXpertz Consultant. Each consultant can be identified by: location, expertise, billing rate, and prior experience rating.
By seamlessly connecting consultants to requesters through a new Kestrel of Merit marketplace, you now will have an easy to use and quicker turnaround to request and staff your consulting needs. Leveraging the KoM app, you can access the subject matter expert you need for your business requirement.

Target Market(s)

Small and medium sized companies; non-profits

Industry/Entity Type

Business Consultant

Contact Information for Business Card

Name
website
email address
Logo
mailing address (debating if I really need...)
twitter
LinkedIn

Requirements
Must have
• the logo I have included in the design; want the colors to be consistent with the logo design

```html
<!DOCTYPE html>
<html lang="en">
<head>
<meta charset="utf-8">
<title>Kestrel of Merit – Business Card</title>
<link rel="stylesheet" href="https://fonts.googleapis.com/css2?family=PT+Sans:wght@400;700&display=swap">
<style>
  :root {
    --navy: #1b2a6b;
    --cyan: #1aa3c9;
    --paper: #ffffff;
    --backdrop: #eceef1;
    --text: #2a2f45;
    --edge: #d9dce3;
  }
  * { box-sizing: border-box; margin: 0; padding: 0; }
  html, body { width: 1200px; height: 900px; overflow: hidden; }
  body {
    background: var(--backdrop);
    font-family: "PT Sans", Arial, sans-serif;
    position: relative;
  }
  .card {
    position: absolute;
    width: 620px;
    height: 354px;
    background: var(--paper);
    border: 1px solid var(--edge);
    box-shadow: 0 6px 18px rgba(20, 30, 60, 0.12);
    overflow: hidden;
  }
  .card--front { left: 290px; top: 50px; }
  .card--back { left: 290px; top: 476px; }

  .brand { display: flex; align-items: center; gap: 14px; color: var(--navy); font-weight: 700; }
  .brand__mark { border: 5px solid var(--navy); border-radius: 50%; flex: none; }
  .card--front .brand {
    position: absolute; left: 0; right: 0; top: 0; bottom: 0;
    flex-direction: column; justify-content: center; gap: 22px;
  }
  .card--front .brand__mark { width: 120px; height: 120px; }
  .card--front .brand__name { font-size: 46px; letter-spacing: 0.5px; }

  .card--back .brand {
    position: absolute; right: 30px; top: 30px;
    flex-direction: column; align-items: flex-end; gap: 10px;
  }
  .card--back .brand__mark { width: 68px; height: 68px; border-width: 4px; margin-right: 58px; }
  .card--back .brand__name { font-size: 25px; }

  .holder {
    position: absolute; left: 40px; top: 58px;
    font-size: 22px; font-weight: 700; color: var(--navy);
  }
  .wave { position: absolute; left: 0; top: 0; width: 620px; height: 354px; }
  .contacts {
    position: absolute; left: 40px; top: 174px;
    list-style: none; font-size: 16px; color: var(--text);
  }
  .contacts li { display: flex; align-items: center; gap: 12px; height: 22px; }
  .contacts svg, .contacts .icon-box { width: 14px; height: 14px; flex: none; }
  .icon-box { background: var(--navy); }
  .address {
    position: absolute; right: 30px; top: 208px;
    text-align: right; color: var(--paper); font-size: 14px; line-height: 1.3;
  }
</style>
</head>
<body>
  <section class="card card--front">
    <div class="brand">
      <span class="brand__mark"></span>
      <span class="brand__name">Kestrel of Merit</span>
    </div>
  </section>

  <section class="card card--back">
    <svg class="wave" viewBox="0 0 620 354" aria-hidden="true">
      <path fill="none" stroke="var(--cyan)" stroke-width="9" d="M0,292 C140,332 255,320 322,260 C372,216 412,186 462,170 C500,160 530,156 560,154"/>
      <path fill="var(--navy)" d="M0,305 C140,345 260,330 330,270 C380,225 420,195 470,180 C520,168 570,162 620,160 L620,354 L0,354 Z"/>
    </svg>
    <h1 class="holder">Marcus Ellery</h1>
    <div class="brand">
      <span class="brand__mark"></span>
      <span class="brand__name">Kestrel of Merit</span>
    </div>
    <ul class="contacts">
      <li>
        <svg viewBox="0 0 14 14"><rect x="0.5" y="2.5" width="13" height="9" fill="var(--navy)"/><path d="M1,3 L7,8 L13,3" fill="none" stroke="#fff" stroke-width="1.2"/></svg>
        info@youremail.com
      </li>
      <li>
        <svg viewBox="0 0 14 14"><circle cx="7" cy="7" r="6.5" fill="var(--navy)"/><g fill="none" stroke="#fff" stroke-width="0.9"><ellipse cx="7" cy="7" rx="2.6" ry="6"/><line x1="1" y1="7" x2="13" y2="7"/><line x1="2" y1="4" x2="12" y2="4"/><line x1="2" y1="10" x2="12" y2="10"/></g></svg>
        www.website.com
      </li>
      <li><span class="icon-box"></span>Yourname/chirpline.com</li>
      <li><span class="icon-box"></span>Yourname/netlinkr.com</li>
    </ul>
    <p class="address">12345, Address Goes Here<br>Country Name, 123456</p>
  </section>
</body>
</html>
```